RepHarborly.com "RE-SKIN" project

We have an existing site that we've recently built that needs to be re-formatted, skinned and polished. Our current developer did an amazing job building the backend but it not an expert in design and formatting of HTML and Web design. We need to have site cleaned up with all new formatting, layout, design elements and visual effects. ALl the date and functionality of the site will remain the same.

We would like to see Home page mock ups that may include Photo's, Flash, etc. or any other design element the designer feels would convey, a corporate, business oriented, simple and clean feel. The way the site currently looks is very basic and we need to have a slick, visual pleasing and easy to navigate design to go with our new functionality. The home page design will then need to translate over into the remaining pages of the site.

This is business to business site and will act as recruitment tool for medical device organizations. We have created a nationwide database of the top medical distributor groups (independent sale reps and groups). We act a "dating site" for medical manufacturers to find the best reps to sell their products.

NOTES on DESIGN:

* THE FUNCTION AND DATA OF THE SITE WILL REMAIN THE SAME, THIS PROJECT WILL BE TAKING ALL EXISTING INFO AND RE-DESIGNING THE LAYOUT.

*Must keep same color scheme

*Home Page design will be main focus and then ALL other pages need to follow style and template of Home page

* The sign up process on the site is in desperate need of re-design and we would like to see BIG, Step by Step, windows that make it feel very simple for the user to fill out (Best example we can think of is the Wellpathory.org site step by step sign up process. As bad as the overall functionality is on that site, the sign up process and drop down menu steps are easy to fill out.)

*The site is currently in a very basic "utilitarian" style and has very little in way of design, text formatting, and overall appearance. We need to have the designer go through each page and JUSTIFY, RE-SIZE, RE-SCALE and dress up all the current information displayed.

* We need the display pages to be easier to read, have better flow and more visually pleasing. (EXAMPLE: ANy search results that are done on the site come back in very table driven, hard to read, small text with small logo. We would like to see more design elements with updated formats and hopefully larger icons and east to read and navigate text

* WE ARE OPEN TO ANY DESIGN IDEAS OR MOCK UPS.

* Logos, icons, animation etc need to remain the same.

*Home page can feature video or photos but the remainder of the site will remian data only.
Updates

We would suggest doing a Mock up of the HOME PAGE only to begin with. We can then evaluate and choose a design theme/concept to carry over into the remainder of the pages.

Target Market(s)

Independent Medical Sales Distributors (sales reps) and Medical device manufacturers.

Industry/Entity Type

Recruitment

Coding

Coded - Design and coding required

Number of Pages Required

5+ page

Font styles to use
Sans Serif

Colors
0492cd
0455a3
3176b5
cedeed
85cae6
fcfdfe

Requirements
Must have
• *Must be Mobile Friendly
• *Must use all the info, links, logos and icons currently on www.RepHarborly.com
• *All pages of the site must follow to layout and design of the Home Page that is created in this project
• *Every page needs to be updated
Nice to have
• Glossy, crisp home page, that incorporate "stock" photos or animation for a more promotional or brochure type of feel
• Easy to navigate, bigger text and buttons and icons.
Should not have
• Color scheme and logo should not change

```html
<!DOCTYPE html>
<html lang="en">
<head>
<meta charset="utf-8">
<title>RepHarborly – Search for Distributors</title>
<link href="https://fonts.googleapis.com/css2?family=Montserrat:wght@500;600;700&family=Open+Sans:wght@400;600;700&display=swap" rel="stylesheet">
<style>
  :root{
    --blue-title:#1c63ad;
    --blue-deep:#0455a3;
    --blue-link:#0492cd;
    --blue-badge:#1d6fbf;
    --green:#7dc243;
    --ink:#222;
    --text:#444;
    --muted:#777;
    --line:#c9c9c9;
    --badge:#a3a3a3;
    --footer:#1b1b1b;
    --footer-line:#3a3a3a;
    --white:#fff;
  }
  *{box-sizing:border-box;margin:0;padding:0}
  html,body{width:690px;height:1200px;overflow:hidden;background:var(--white)}
  body{font-family:"Open Sans",sans-serif;color:var(--text)}
  .canvas{position:relative;width:690px;height:1200px;overflow:hidden}
  .abs{position:absolute}

  /* header */
  .site-header{position:absolute;left:0;top:0;width:690px;height:54px;border-bottom:2px solid #e2e2e2;box-shadow:0 1px 2px rgba(0,0,0,.06)}
  .brand{position:absolute;display:flex;align-items:center;gap:5px;font-family:"Open Sans",sans-serif;font-weight:700}
  .brand-mark{width:20px;height:20px;background:var(--blue-badge);border-radius:3px}
  .site-header .brand{left:56px;top:16px;font-size:17px;color:var(--ink)}
  .main-nav a{position:absolute;top:19px;font-family:"Montserrat",sans-serif;font-weight:600;font-size:8.6px;color:var(--ink);text-decoration:none;letter-spacing:.1px}
  .main-nav a.is-active{color:var(--green)}
  .nav-search{position:absolute;left:546px;top:20px}
  .login-btn{position:absolute;left:574px;top:13px;width:59px;height:26px;border:2px solid var(--green);border-radius:14px;display:flex;align-items:center;justify-content:center;gap:3px;font-family:"Montserrat",sans-serif;font-weight:700;font-size:8.6px;color:var(--green)}

  /* breadcrumb */
  .breadcrumb{left:56px;top:76px;font-family:"Montserrat",sans-serif;font-weight:600;font-size:8px;color:var(--ink)}
  .breadcrumb .sep{margin:0 5px}
  .breadcrumb .current{color:var(--blue-link)}
  .rule{left:56px;top:101px;width:578px;height:1px;background:#d6d6d6}

  .page-title{left:0;top:146px;width:690px;text-align:center;font-family:"Montserrat",sans-serif;font-weight:600;font-size:20px;line-height:29px;color:var(--blue-title)}
  .quick-search-label{left:134px;top:230px;font-family:"Montserrat",sans-serif;font-weight:600;font-size:8.6px;color:var(--ink)}
  .quick-search{left:186px;top:223px;width:369px;height:26px;border:1px solid var(--line);font-size:8px;color:#666;padding:7px 9px}

  /* search panel */
  .panel{left:56px;top:301px;width:578px;height:630px;border:1px solid var(--line)}
  .panel-heading{left:0;top:289px;width:690px;display:flex;justify-content:center}
  .panel-heading span.wrap{background:var(--white);padding:0 10px;display:flex;align-items:center;gap:6px;font-family:"Montserrat",sans-serif;font-weight:600;font-size:15.5px;color:var(--ink)}
  .count-badge{background:var(--blue-badge);color:var(--white);padding:2px 4px;line-height:19px}

  .field-label{position:absolute;right:370px;text-align:right;font-size:8.8px;line-height:13px;color:#333}
  .select{position:absolute;left:345px;width:274px;height:27px;border:1px solid #b9b9b9;font-size:8px;color:#555}
  .select .value{position:absolute;left:13px;top:7px}
  .select .count{position:absolute;right:34px;top:5px;width:24px;height:17px;background:var(--badge);color:var(--white);font-weight:700;font-size:8.6px;text-align:center;line-height:17px}
  .select .divider{position:absolute;right:28px;top:0;width:1px;height:25px;background:#b9b9b9}
  .select .caret{position:absolute;right:10px;top:11px}
  .text-input{position:absolute;left:345px;width:274px;height:27px;border:1px solid #b9b9b9}

  .radio-group{left:345px;top:477px;display:flex;gap:11px;font-size:8px;color:#444}
  .radio{display:flex;align-items:center;gap:4px}
  .radio i{width:9px;height:9px;border:1.5px solid #777;border-radius:50%;display:inline-block;position:relative}
  .radio.checked i{border-color:var(--blue-badge)}
  .radio.checked i::after{content:"";position:absolute;left:1.5px;top:1.5px;width:3px;height:3px;border-radius:50%;background:var(--blue-badge)}

  .sub-heading{left:0;top:569px;width:690px;text-align:center;font-family:"Montserrat",sans-serif;font-weight:600;font-size:15.5px;line-height:22px;color:var(--ink)}
  .feature-list{left:345px;top:636px;list-style:none;font-size:8px;color:#555}
  .feature-list li{display:flex;align-items:center;gap:6px;height:15.3px}

  .search-btn{left:306px;top:870px;width:78px;height:30px;border-radius:16px;background:var(--green);color:var(--white);font-family:"Montserrat",sans-serif;font-weight:600;font-size:11px;display:flex;align-items:center;justify-content:center}

  /* footer */
  .site-footer{left:0;top:986px;width:690px;height:214px;background:var(--footer);color:var(--white)}
  .site-footer .brand{left:58px;top:71px;font-size:17px;color:var(--white)}
  .site-footer .brand-mark{background:var(--white)}
  .socials{left:86px;top:110px;display:flex;gap:5px}
  .socials span{width:18px;height:18px;border:1px solid #cfcfcf;border-radius:50%}
  .footer-heading{position:absolute;top:41px;font-family:"Montserrat",sans-serif;font-weight:600;font-size:10.4px}
  .quick-links{left:231px;top:64px;list-style:none;font-size:7px;line-height:14.4px}
  .news-text{left:332px;top:68px;font-size:7px;line-height:12px}
  .news-input{left:332px;top:98px;width:146px;height:20px;background:var(--white);color:#777;font-size:6.6px;padding:5px 8px}
  .subscribe{left:331px;top:127px;width:63px;height:21px;border-radius:11px;background:var(--green);font-size:6.6px;font-weight:600;display:flex;align-items:center;justify-content:center}
  .contact{position:absolute;left:518px;font-size:7px;line-height:12px;display:flex;gap:10px}
  .contact svg{flex:none;margin-top:1px}
  .footer-rule{left:56px;top:165px;width:578px;height:1px;background:var(--footer-line)}
  .copyright{left:0;top:183px;width:690px;text-align:center;font-size:7px}
</style>
</head>
<body>
<div class="canvas">

  <header class="site-header">
    <div class="brand"><span class="brand-mark"></span>RepHarborly.com</div>
    <nav class="main-nav">
      <a style="left:239px">HOW IT WORKS</a>
      <a style="left:320px">SIGNUP</a>
      <a style="left:368px">PRODUCTS</a>
      <a style="left:430px" class="is-active">SEARCH</a>
      <a style="left:480px">RESOURCES</a>
    </nav>
    <svg class="nav-search" width="10" height="10" viewBox="0 0 10 10"><circle cx="4" cy="4" r="3" fill="none" stroke="#222" stroke-width="1.6"/><line x1="6.2" y1="6.2" x2="9" y2="9" stroke="#222" stroke-width="1.8"/></svg>
    <div class="login-btn"><svg width="7" height="8" viewBox="0 0 7 8"><rect x="0" y="3.3" width="7" height="4.7" rx="0.8" fill="#7dc243"/><path d="M1.6 3.5V2.3a1.9 1.9 0 0 1 3.8 0v1.2" fill="none" stroke="#7dc243" stroke-width="1.1"/></svg>LOGIN</div>
  </header>

  <div class="abs breadcrumb">HOME<span class="sep">&gt;&gt;</span>SEARCH<span class="sep">&gt;&gt;</span><span class="current">SEARCH FOR DISTRIBUTORS</span></div>
  <div class="abs rule"></div>

  <h1 class="abs page-title">LOCATE AND SECURE THE TOP<br>DISTRIBUTORS IN THE MEDICAL INDUSTRY!</h1>

  <div class="abs quick-search-label">SEARCH</div>
  <div class="abs quick-search">Results (0)</div>

  <section class="abs panel"></section>
  <div class="abs panel-heading"><span class="wrap">SEARCH <span class="count-badge">144</span> DISTRIBUTORS</span></div>

  <div class="field-label" style="top:354px">In What States do you want representation? :</div>
  <div class="select" style="top:347px"><span class="value">Any States</span><span class="count">51</span><span class="divider"></span><svg class="caret" width="7" height="4" viewBox="0 0 7 4"><path d="M0 0h7L3.5 4z" fill="#555"/></svg></div>

  <div class="field-label" style="top:393px">What PRODUCT CATEGORY does your product line fall into? :</div>
  <div class="select" style="top:386px"><span class="value">Any Facilities Types</span><span class="count">14</span><span class="divider"></span><svg class="caret" width="7" height="4" viewBox="0 0 7 4"><path d="M0 0h7L3.5 4z" fill="#555"/></svg></div>

  <div class="field-label" style="top:433px">What type of Call Points – Facility do you sell into?:</div>
  <div class="select" style="top:426px"><span class="value">Any Market Segments</span><span class="count">16</span><span class="divider"></span><svg class="caret" width="7" height="4" viewBox="0 0 7 4"><path d="M0 0h7L3.5 4z" fill="#555"/></svg></div>

  <div class="field-label" style="top:469px;text-align:center;width:260px;right:370px">Do you currently have a non-compete in place for any<br>specifics areas (Total Joint, Wound, Cardiac, Bracing etc)?:*</div>
  <div class="abs radio-group">
    <span class="radio checked"><i></i>Any</span>
    <span class="radio"><i></i>Yes</span>
    <span class="radio"><i></i>No</span>
  </div>

  <div class="field-label" style="top:517px">Distributor Annual Sales :</div>
  <div class="select" style="top:510px"><span class="value">Any Sales</span><span class="divider"></span><svg class="caret" width="7" height="4" viewBox="0 0 7 4"><path d="M0 0h7L3.5 4z" fill="#555"/></svg></div>

  <h2 class="abs sub-heading">SECURE THE TOP MEDICAL DISTRIBUTION<br>GROUPS AND REPS ALL IN ONE PLACE!</h2>

  <div class="field-label" style="top:636px">Search For Distributors By:</div>
  <ul class="abs feature-list">
    <li><svg width="8" height="8" viewBox="0 0 8 8"><circle cx="4" cy="4" r="4" fill="#1d6fbf"/><path d="M2 4.1l1.4 1.3L6 2.8" fill="none" stroke="#fff" stroke-width="1.1"/></svg>State(s)</li>
    <li><svg width="8" height="8" viewBox="0 0 8 8"><circle cx="4" cy="4" r="4" fill="#1d6fbf"/><path d="M2 4.1l1.4 1.3L6 2.8" fill="none" stroke="#fff" stroke-width="1.1"/></svg>Product Categories</li>
    <li><svg width="8" height="8" viewBox="0 0 8 8"><circle cx="4" cy="4" r="4" fill="#1d6fbf"/><path d="M2 4.1l1.4 1.3L6 2.8" fill="none" stroke="#fff" stroke-width="1.1"/></svg>Non compete</li>
    <li><svg width="8" height="8" viewBox="0 0 8 8"><circle cx="4" cy="4" r="4" fill="#1d6fbf"/><path d="M2 4.1l1.4 1.3L6 2.8" fill="none" stroke="#fff" stroke-width="1.1"/></svg>Facility and Surgeon Relationships</li>
    <li><svg width="8" height="8" viewBox="0 0 8 8"><circle cx="4" cy="4" r="4" fill="#1d6fbf"/><path d="M2 4.1l1.4 1.3L6 2.8" fill="none" stroke="#fff" stroke-width="1.1"/></svg>PLUS YOU CAN bulk message several distributor at once and save time!</li>
  </ul>

  <div class="field-label" style="top:732px">What Surgeon relationships you would prefer the<br>distributor to have?:</div>
  <div class="select" style="top:732px"><span class="value">Any States</span><span class="count">51</span><span class="divider"></span><svg class="caret" width="7" height="4" viewBox="0 0 7 4"><path d="M0 0h7L3.5 4z" fill="#555"/></svg></div>

  <div class="field-label" style="top:779px">Keywords:</div>
  <div class="text-input" style="top:772px"></div>

  <div class="field-label" style="top:820px">Posted Within :</div>
  <div class="select" style="top:813px"><span class="value">Any Date Range</span><span class="divider"></span><svg class="caret" width="7" height="4" viewBox="0 0 7 4"><path d="M0 0h7L3.5 4z" fill="#555"/></svg></div>

  <div class="abs search-btn">SEARCH</div>

  <footer class="abs site-footer">
    <div class="brand"><span class="brand-mark"></span>RepHarborly.com</div>
    <div class="abs socials"><span></span><span></span><span></span><span></span></div>

    <div class="footer-heading" style="left:231px">QUICK LINKS</div>
    <ul class="abs quick-links">
      <li>Help</li><li>FAQ</li><li>Support</li><li>Sitemap</li><li>Terms Of Use</li><li>Privacy Statement</li>
    </ul>

    <div class="footer-heading" style="left:332px">NEWSLETTER SUBSCRIPTION</div>
    <p class="abs news-text">Register your Email Address to get<br>Information about us</p>
    <div class="abs news-input">Email Address</div>
    <div class="abs subscribe">SUBSCRIBE</div>

    <div class="footer-heading" style="left:518px">CONTACT US</div>
    <div class="contact" style="top:67px"><svg width="6" height="8" viewBox="0 0 6 8"><path d="M3 0a3 3 0 0 1 3 3c0 2-3 5-3 5S0 5 0 3a3 3 0 0 1 3-3z" fill="#fff"/><circle cx="3" cy="3" r="1" fill="#1b1b1b"/></svg><span>1180 NW ALDER CREST RD<br>#210 FAIRVIEW, OR 97204</span></div>
    <div class="contact" style="top:103px"><svg width="7" height="7" viewBox="0 0 7 7"><path d="M1.3 0l1.3 1.8-.8.9a4.6 4.6 0 0 0 2.5 2.5l.9-.8L7 5.7 6 7C2.8 7 0 4.2 0 1z" fill="#fff"/></svg><span>1 800 555 0142</span></div>
    <div class="contact" style="top:127px"><svg width="8" height="6" viewBox="0 0 8 6"><rect width="8" height="6" fill="#fff"/><path d="M0 0l4 3.2L8 0" fill="none" stroke="#1b1b1b" stroke-width=".8"/></svg><span>info@repharborly.com</span></div>

    <div class="abs footer-rule"></div>
    <p class="abs copyright">Copyrights © 2018, RepHarborly. All rights reserved.</p>
  </footer>

</div>
</body>
</html>
```